International instant Date Coffee

We have a new instant coffee (5 In 1) product with a highly rich ingredient (date and Kernel Of date). Each box has 10 satiates.
*New instant coffee with DATES ( 5 in 1 ). we would like the design show majority of Coffee and date with Arab traditional or background.
* Ingredients: Coffee,Date,Date Kernel, Sugar,nondairy cream).
* Natural 100% and no artificial flavors or colors.
* Made In Malaysia.
* Arabic language should be in the design (I will provide you what you need later).
* Name of the product ( SOLEK CAFE)

Target Market(s)

International,with special touch of Arabic sense

Industry/Entity Type

Food Store

Font styles to use
Serif

Requirements
Must have
• My project must have Coffee beans,dates and some things related to Arab Natural.
Nice to have
• My project must have Coffee beans,dates and some things related to Arab Natural. Suitable for international market
Should not have
• should be cool and not flashy.

```html
<!DOCTYPE html>
<html lang="en">
<head>
<meta charset="utf-8">
<title>Solek Cafe – Label Options</title>
<link rel="stylesheet" href="https://fonts.googleapis.com/css2?family=Changa:wght@700;800&family=Great+Vibes&family=Lobster&family=Teko:wght@500&family=Passion+One:wght@400&family=Oswald:wght@600&family=Comfortaa:wght@400&family=Yanone+Kaffeesatz:wght@500&display=swap">
<style>
  :root {
    --sheet: #fdfaa6;
    --marker: #ffb400;
    --marker-text: #d41a00;
    --brand-red: #e8141a;
    --white: #ffffff;
    --maroon: #4a0f10;
    --badge-red: #c4121c;
    --sky-palm: #4b5a2c;
    --sand: #e6b867;
    --sand-deep: #c98e3e;
    --copper: #b4662e;
  }
  * { margin: 0; padding: 0; box-sizing: border-box; }
  html, body { width: 1005px; height: 1200px; overflow: hidden; background: var(--sheet); }
  .sheet { position: relative; width: 1005px; height: 1200px; }

  .option-number {
    position: absolute; width: 60px; height: 52px; border-radius: 50%;
    background: var(--marker); color: var(--marker-text);
    font: 800 38px/52px "Changa", sans-serif; text-align: center;
  }

  .label { position: absolute; overflow: hidden; }
  .label-photo {
    position: absolute; inset: 0;
    background:
      radial-gradient(ellipse 22% 40% at 82% 82%, var(--copper), rgba(180,102,46,0) 100%),
      linear-gradient(180deg, var(--sky-palm) 0%, #7b6a3a 22%, var(--sand) 45%, #efc37a 70%, var(--sand-deep) 100%);
  }
  .label > *:not(.label-photo) { position: absolute; }

  .ar-top { font-family: "Changa", sans-serif; font-weight: 800; line-height: 1; direction: rtl; white-space: nowrap; }
  .ar-white { color: var(--white); text-shadow: 0 2px 3px rgba(0,0,0,.5); }
  .ar-red { color: var(--brand-red); text-shadow: 0 2px 3px rgba(0,0,0,.35); }
  .ar-sub { font-family: "Changa", sans-serif; font-weight: 700; color: var(--maroon); direction: rtl; white-space: nowrap; }

  .brand-name { color: var(--maroon); white-space: nowrap; line-height: 1; text-shadow: 0 0 3px #fff, 0 0 2px #fff; }
  .brand-script { font-family: "Great Vibes", cursive; }
  .brand-lobster { font-family: "Lobster", cursive; }
  .brand-block { font-family: "Passion One", sans-serif; letter-spacing: 1px; }
  .brand-caps { font-family: "Oswald", sans-serif; font-weight: 600; letter-spacing: 2px; }

  .badge {
    border-radius: 50%; background: radial-gradient(circle at 40% 35%, #e8323a, var(--badge-red) 60%, #7d0a10);
    color: var(--white); font-family: "Changa", sans-serif; font-weight: 700;
    display: flex; align-items: center; justify-content: center; white-space: nowrap;
  }
  .badge small { font-size: 0.55em; margin: 0 1px; }

  .tagline { color: var(--white); line-height: 1.15; text-shadow: 0 1px 2px rgba(0,0,0,.7); white-space: nowrap; }
  .tag-teko { font-family: "Teko", sans-serif; font-weight: 500; letter-spacing: 1px; }
  .tag-yanone { font-family: "Yanone Kaffeesatz", sans-serif; font-weight: 500; }
  .tag-round { font-family: "Comfortaa", sans-serif; color: #fff8e0; }
</style>
</head>
<body>
<main class="sheet">

  <div class="option-number" style="left:239px;top:0">1</div>
  <div class="option-number" style="left:695px;top:0">2</div>
  <div class="option-number" style="left:228px;top:376px">3</div>
  <div class="option-number" style="left:695px;top:376px">4</div>
  <div class="option-number" style="left:469px;top:756px">5</div>

  <!-- Option 1 -->
  <section class="label" style="left:57px;top:56px;width:479px;height:310px">
    <div class="label-photo" role="img" aria-label="Desert dunes with date palms, a copper coffee pot and a sack of coffee beans"></div>
    <div class="ar-top ar-red" style="right:12%;top:6%;font-size:68px;transform:rotate(-8deg)">سولك</div>
    <div class="ar-top ar-white" style="right:26%;top:30%;font-size:50px">كافيه</div>
    <div class="ar-sub" style="right:23%;top:52%;font-size:14px">(التمر &amp; النواة)</div>
    <div class="brand-name brand-script" style="left:9%;top:59%;font-size:58px">Solek Cafe</div>
    <div class="badge" style="left:5%;top:76%;width:52px;height:52px;font-size:22px">5<small>IN</small>1</div>
    <div class="tagline tag-teko" style="left:22%;top:77%;font-size:19px">ARABIC DATE COFFEE<br>SPECIAL TASTE</div>
  </section>

  <!-- Option 2 -->
  <section class="label" style="left:536px;top:56px;width:442px;height:310px">
    <div class="label-photo" role="img" aria-label="Desert dunes with date palms, a copper coffee pot and a sack of coffee beans"></div>
    <div class="ar-top ar-white" style="right:21%;top:5%;font-size:56px">سولك</div>
    <div class="ar-top ar-red" style="right:11%;top:25%;font-size:56px">قەهوەی</div>
    <div class="ar-sub" style="right:15%;top:53%;font-size:13px">(التمر &amp; النواة)</div>
    <div class="brand-name brand-block" style="left:6%;top:63%;font-size:38px">Solek Cafe</div>
    <div class="badge" style="left:5%;top:79%;width:48px;height:48px;font-size:20px">5<small>IN</small>1</div>
    <div class="tagline tag-teko" style="left:21%;top:79%;font-size:17px">ARABIC DATE COFFEE<br>SPECIAL TASTE</div>
  </section>

  <!-- Option 3 -->
  <section class="label" style="left:61px;top:437px;width:438px;height:309px">
    <div class="label-photo" role="img" aria-label="Desert dunes with date palms, a copper coffee pot and a sack of coffee beans"></div>
    <div class="ar-top ar-white" style="right:19%;top:7%;font-size:54px">سولك</div>
    <div class="ar-top ar-red" style="right:9%;top:27%;font-size:56px">قەهوەی</div>
    <div class="ar-sub" style="right:12%;top:53%;font-size:13px">(التمر &amp; النواة)</div>
    <div class="brand-name brand-lobster" style="left:7%;top:63%;font-size:40px">SolekCafe</div>
    <div class="badge" style="left:5%;top:80%;width:46px;height:46px;font-size:19px">5<small>IN</small>1</div>
    <div class="tagline tag-teko" style="left:22%;top:80%;font-size:17px">ARABIC DATE COFFEE<br>SPECIAL TASTE</div>
  </section>

  <!-- Option 4 -->
  <section class="label" style="left:524px;top:435px;width:449px;height:310px">
    <div class="label-photo" role="img" aria-label="Desert dunes with date palms, a copper coffee pot and a sack of coffee beans"></div>
    <div class="ar-top ar-white" style="right:19%;top:6%;font-size:56px">سولك</div>
    <div class="ar-top ar-red" style="right:12%;top:27%;font-size:56px">قەهوەی</div>
    <div class="ar-sub" style="right:11%;top:54%;font-size:13px">(التمر &amp; النواة)</div>
    <div class="brand-name brand-script" style="left:8%;top:62%;font-size:44px;font-family:'Lobster',cursive">Solek Cafe</div>
    <div class="badge" style="left:5%;top:80%;width:48px;height:48px;font-size:20px">5<small>IN</small>1</div>
    <div class="tagline tag-yanone" style="left:21%;top:81%;font-size:16px">Arabic Date Coffee<br>Special Taste</div>
  </section>

  <!-- Option 5 -->
  <section class="label" style="left:205px;top:814px;width:590px;height:376px">
    <div class="label-photo" role="img" aria-label="Desert dunes with date palms, a copper coffee pot and a sack of coffee beans"></div>
    <div class="ar-top ar-white" style="right:23%;top:6%;font-size:74px">سولك</div>
    <div class="ar-top ar-red" style="right:13%;top:32%;font-size:74px">قەهوەی</div>
    <div class="ar-sub" style="right:13%;top:57%;font-size:16px">(التمر &amp; النواة)</div>
    <div class="brand-name brand-caps" style="left:5%;top:68%;font-size:40px">SOLEK CAFE</div>
    <div class="badge" style="left:5%;top:81%;width:62px;height:62px;font-size:26px">5<small>IN</small>1</div>
    <div class="tagline tag-round" style="left:20%;top:83%;font-size:19px">Arabic Date Coffee<br>Special Taste</div>
  </section>

</main>
</body>
</html>
```